Speisekarten-Design für Gastronomiebetrieb
Zielgruppe
Wir sind ein Gastronomiebetrieb in einer Studentenstadt. Unsere Hauptzielgruppe sind junge Menschen und Studenten, aber auch älteres Puplikum. Wir möchten gerne ein neues Speisekartendesign, da unser aktuelles seit über 10 Jahren sich kaum verändert hat.
Aufgabenstellung
Gerne könne Sie sich die aktulle Speisekarte auf der unserer Hompeage anschauen: www.tomello-kassel.de
Auf der Frontseite soll die Farbrichtung Orange und natürlich das Logo beibehalten werden. Für die restlichen Seiten gibt es diese Einschränkung nicht. Uns ist wichtig, dass die Speisekarte modern, bunt und peppig ist. Das heisst möglichst mit kräftigen Farben und Bildern von Speisen und Getränken arbeiten.

```html
<!DOCTYPE html>
<html lang="de">
<head>
<meta charset="utf-8">
<title>Tomello – Speisekarte</title>
<link rel="stylesheet" href="https://fonts.googleapis.com/css2?family=Barlow+Condensed:wght@500;800&display=swap">
<style>
  :root {
    --amber: #fab200;
    --amber-deep: #f7aa00;
    --orange: #ef8200;
    --orange-red: #e85a10;
    --signal-red: #e3110f;
    --brand-red: #e2071a;
    --tagline-red: #a2160f;
  }
  html, body {
    margin: 0;
    padding: 0;
    width: 848px;
    height: 1200px;
    overflow: hidden;
  }
  .menu-cover {
    position: relative;
    width: 848px;
    height: 1200px;
    background: linear-gradient(
      to bottom,
      var(--amber) 0%,
      var(--amber-deep) 45%,
      var(--orange) 58%,
      var(--orange-red) 76%,
      var(--signal-red) 100%
    );
    font-family: "Barlow Condensed", "Arial Narrow", sans-serif;
  }
  .brand-name {
    position: absolute;
    top: 268px;
    left: 0;
    width: 848px;
    margin: 0;
    text-align: center;
    font-weight: 800;
    font-size: 158px;
    line-height: 1;
    letter-spacing: 4px;
    color: var(--brand-red);
  }
  .brand-tagline {
    position: absolute;
    top: 432px;
    left: 0;
    width: 848px;
    margin: 0;
    text-align: center;
    font-weight: 500;
    font-size: 44px;
    line-height: 1;
    letter-spacing: 2px;
    color: var(--tagline-red);
  }
  .brand-tagline .separator {
    display: inline-block;
    margin: 0 10px;
    font-size: 30px;
    vertical-align: 4px;
  }
</style>
</head>
<body>
  <main class="menu-cover">
    <h1 class="brand-name">TOMELLO</h1>
    <p class="brand-tagline">CAFÉ<span class="separator">•</span>BAR<span class="separator">•</span>RESTAURANT</p>
  </main>
</body>
</html>
```